GLOW ON THE AVENUE WEBSITE

I have a website www.glowontheavenue.org , need information from that jazzed up. wanted page to be fun & funky .

Target Market(s)

18 to 35yrs guys & girls

Requirements
Must have
• use all photos on website, need to attached my brochure for printing

```html
<!DOCTYPE html>
<html lang="en">
<head>
<meta charset="utf-8">
<title>Glow on the Avenue</title>
<link rel="stylesheet" href="https://fonts.googleapis.com/css2?family=Arimo:ital,wght@0,400;0,700;1,400;1,700&family=Libre+Baskerville&family=Questrial&display=swap">
<style>
  :root {
    --page-bg: #f2efe9;
    --brand-red: #ea4446;
    --tile-red: #ee7676;
    --white: #ffffff;
    --text-dark: #3a3a3a;
    --rule: #7a7a7a;
    --footer-bg: #474546;
    --footer-text: #c9c9c9;
    --quote-mark: #f49a9a;
  }
  * { box-sizing: border-box; margin: 0; padding: 0; }
  html, body { width: 1153px; height: 1200px; overflow: hidden; }
  body { background: var(--page-bg); font-family: "Arimo", Arial, sans-serif; }
  .site { position: absolute; left: 159px; top: 0; width: 836px; height: 1200px; background: var(--white); }

  .site-header { position: absolute; left: 0; top: 0; width: 836px; height: 97px; background: var(--brand-red); }
  .brand { position: absolute; left: 13px; top: 20px; font-family: "Libre Baskerville", Georgia, serif; font-size: 24px; color: var(--white); letter-spacing: 0.5px; }
  .social { position: absolute; right: 12px; top: 9px; display: flex; gap: 10px; }
  .social span { width: 29px; height: 29px; border-radius: 50%; background: rgba(255,255,255,0.45); display: block; }
  .main-nav { position: absolute; left: 5px; right: 5px; top: 74px; display: flex; justify-content: space-between; }
  .main-nav a { color: var(--white); font-size: 11.5px; text-decoration: none; }

  .feature-grid { position: absolute; left: 0; top: 127px; width: 836px; display: grid; grid-template-columns: repeat(4, 209px); grid-auto-rows: 213px; }
  .tile { position: relative; }
  .tile-offer { background: var(--tile-red); color: var(--white); font-family: "Libre Baskerville", Georgia, serif; text-align: center; }
  .tile-offer h3 { font-weight: 400; font-size: 19px; margin-top: 48px; }
  .tile-offer p { font-size: 13px; line-height: 27px; margin-top: 34px; }
  .tile-offer.lower h3 { margin-top: 37px; }
  .photo-waxing { background: linear-gradient(160deg, #f3e2d6, #dcbca6); }
  .photo-lipstick { background: linear-gradient(90deg, #fbeee6, #f1d6cf); }
  .photo-towels { background: linear-gradient(160deg, #e9b04a, #d9cfb8 60%, #b99a62); }
  .photo-lashes { background: linear-gradient(160deg, #f4f0ee, #d9ccc4); }

  .tagline { position: absolute; left: 0; width: 836px; top: 593px; text-align: center; font-family: "Questrial", sans-serif; font-size: 26px; color: var(--text-dark); }
  .tagline .brand-inline { font-family: "Libre Baskerville", Georgia, serif; color: var(--brand-red); font-size: 24px; margin-left: 12px; }
  .divider { position: absolute; left: 8px; top: 666px; width: 820px; height: 2px; background: var(--rule); }

  .why-photo { position: absolute; left: 128px; top: 700px; width: 234px; height: 162px; background: linear-gradient(180deg, #d7c3b6, #f4ece6); }
  .why-us { position: absolute; left: 480px; top: 700px; }
  .why-us h2 { font-family: "Questrial", sans-serif; font-weight: 400; font-size: 26px; color: var(--brand-red); }
  .why-us ul { list-style: none; margin-top: 20px; }
  .why-us li { font-family: "Questrial", sans-serif; font-size: 15px; color: var(--text-dark); height: 23px; position: relative; padding-left: 25px; }
  .why-us li::before { content: ""; position: absolute; left: 6px; top: 5px; width: 5px; height: 5px; border-radius: 50%; background: var(--brand-red); }

  .testimonials { position: absolute; left: 0; top: 920px; width: 836px; height: 184px; background: var(--brand-red); }
  .quote { position: absolute; width: 240px; color: var(--white); font-style: italic; font-weight: 700; font-size: 10.5px; line-height: 23px; padding-left: 56px; }
  .quote::before { content: "\201D"; position: absolute; left: 14px; top: -16px; font-family: Georgia, serif; font-style: normal; font-size: 58px; color: var(--quote-mark); }
  .quote cite { display: block; text-align: right; padding-right: 30px; font-style: italic; }
  .q1 { left: 0; top: 37px; width: 265px; }
  .q2 { left: 287px; top: 37px; width: 265px; }
  .q3 { left: 570px; top: 57px; width: 266px; }

  .site-footer { position: absolute; left: 0; top: 1143px; width: 836px; height: 57px; background: var(--footer-bg); }
  .site-footer p { position: absolute; left: 53px; top: 24px; font-size: 11px; font-style: italic; color: var(--footer-text); }
  .site-footer .social { top: 15px; right: 53px; }
  .site-footer .social span { background: #7e7c7d; }
</style>
</head>
<body>
<div class="site">
  <header class="site-header">
    <div class="brand">GLOW ON THE AVENUE</div>
    <div class="social" aria-label="Social links"><span></span><span></span><span></span></div>
    <nav class="main-nav">
      <a href="#">HOME</a><a href="#">WAXING</a><a href="#">BROWS</a><a href="#">LASHES</a><a href="#">TANNING</a><a href="#">HANDS&amp;FEET</a><a href="#">FACIALS&amp;MASSAGE</a><a href="#">MAKEUP</a><a href="#">SPECIALS</a><a href="#">PRODUCTS</a><a href="#">BLOG</a><a href="#">CONTACT US</a>
    </nav>
  </header>

  <section class="feature-grid">
    <div class="tile photo-waxing" role="img" aria-label="Bikini waxing photo with a blue ribbon"></div>
    <div class="tile tile-offer"><h3>Best Tanning</h3><p>Lorem ipsum sud<br>dolor, dummy text</p></div>
    <div class="tile photo-lipstick" role="img" aria-label="Row of pink lipsticks"></div>
    <div class="tile tile-offer"><h3>Best Tanning</h3><p>Lorem ipsum sud<br>dolor, dummy text</p></div>
    <div class="tile tile-offer lower"><h3>Best Tanning</h3><p>Lorem ipsum sud<br>dolor, dummy text</p></div>
    <div class="tile photo-towels" role="img" aria-label="Folded spa towels with lilies"></div>
    <div class="tile tile-offer lower"><h3>Best Tanning</h3><p>Lorem ipsum sud<br>dolor, dummy text</p></div>
    <div class="tile photo-lashes" role="img" aria-label="Close-up of long eyelashes"></div>
  </section>

  <p class="tagline">For the best wax down under visit <span class="brand-inline">GLOW ON THE AVENUE</span></p>
  <div class="divider"></div>

  <div class="why-photo" role="img" aria-label="Smiling woman with long hair"></div>
  <section class="why-us">
    <h2>Why choose us</h2>
    <ul>
      <li>Lorem ipsum sample</li><li>Lorem ipsum sample</li><li>Lorem ipsum sample</li><li>Lorem ipsum sample</li><li>Lorem ipsum sample</li>
    </ul>
  </section>

  <section class="testimonials">
    <blockquote class="quote q1">Lorem ipsum dolor sit amet, consectetur adipiscing elit. Nulla aliquam tincidunt nibh imperdiet rutrum. Cras sit amet nibh sem, in pulvinar velit.<cite>– Jon Doe</cite></blockquote>
    <blockquote class="quote q2">Lorem ipsum dolor sit amet, consectetur adipiscing elit. Nulla aliquam tincidunt nibh imperdiet rutrum. Cras sit amet nibh sem, in pulvinar velit.<cite>– Jon Doe</cite></blockquote>
    <blockquote class="quote q3">Lorem ipsum dolor sit amet, consectetur adipiscing elit. Nulla aliquam tincidunt nibh imperdiet rutrum. Cras sit amet nibh sem, in pulvinar velit.<cite>– Jon Doe</cite></blockquote>
  </section>

  <footer class="site-footer">
    <p>All Rights Reserved R GLOW ON THE AVENUE 2013</p>
    <div class="social" aria-label="Social links"><span></span><span></span><span></span></div>
  </footer>
</div>
</body>
</html>
```